Nobody Left the Lantern Burning - Tom Halvery - CD Cover Design Project

Single Cover for CD & Online media e.g. Tunebox Graphics
The first song release from Tom Halvery will be the track 'Nobody Left the Lantern Burning'.
For the release the single requires artwork that is eye catching, seriously professional & meets the requirements of Disc Sprout, Tunebox and also a physical copy on CD.
Track listings for CD will be:
1. Nobody Left the Lantern Burning
2. Nobody Left the Lantern Burning - Instrumental
see details in this link:
http://members.discsprout-example.com/faq.aspx
http://selfmadesound.discsprout-example.com/2009/11/avoid-album-art-atrocities/
http://answers.quorvex-example.com/question/index?qid=20111015141433AAdDTmH
Any advice on this would be greatly appreciated,
I would also like the two logo's I have uploaded to be used,
one is the Tom Halvery logo and the other is for Milbrook & Tandy Records logo (please remove the R and replace with a C for copyright.)
There are four high res photo shopped pictures of Tom Halvery and another zip file of many others, it would be nice to include one of these maybe on the 2nd page or back of the CD. Please don't use them as the front cover.
I imagine an Art Deco illustration but please listen to the track and let it inspire you.
Good Luck
Updates
I don't feel this is what I'm looking for, the design needs to refelct a broken heart without being a picture of a broken heart
Reason: No design has been what we are after so far so the deadline has been extended and the budget increased.

```html
<!DOCTYPE html>
<html lang="en">
<head>
<meta charset="utf-8">
<title>Nobody Left the Lantern Burning — Tom Halvery</title>
<link href="https://fonts.googleapis.com/css2?family=Cabin:wght@500&family=Josefin+Sans:wght@300&family=Uncial+Antiqua&display=swap" rel="stylesheet">
<style>
  :root {
    --ink: #0b0906;
    --umber-deep: #140a04;
    --umber: #3d2109;
    --rust: #6e2a0c;
    --moss: #6f9f2c;
    --lime: #9cc843;
    --lime-pale: #b8d95a;
    --art-red: #e4321c;
    --art-red-soft: rgba(228, 50, 28, 0.85);
    --art-red-fade: rgba(200, 40, 20, 0);
    --name-gold: #c9d44c;
    --line-cream: #f2e6a0;
  }
  html, body {
    margin: 0;
    padding: 0;
    width: 1200px;
    height: 1200px;
    overflow: hidden;
    background: var(--ink);
  }
  .cover {
    position: relative;
    width: 1200px;
    height: 1200px;
    overflow: hidden;
  }
  .cover-backdrop {
    position: absolute;
    inset: 0;
    background:
      radial-gradient(ellipse 420px 600px at 160px 620px, var(--rust) 0%, transparent 70%),
      linear-gradient(90deg, var(--umber-deep) 0%, var(--umber) 30%, #4f5a18 46%, var(--moss) 60%, var(--lime) 80%, var(--lime-pale) 100%);
  }
  .centre-artwork {
    position: absolute;
    left: 150px;
    top: 140px;
    width: 970px;
    height: 930px;
    background: radial-gradient(ellipse 50% 50% at 50% 48%, var(--art-red) 0%, var(--art-red-soft) 55%, var(--art-red-fade) 100%);
  }
  .name-band {
    position: absolute;
    left: 590px;
    top: 356px;
    width: 417px;
    height: 66px;
    background: var(--ink);
    display: flex;
    align-items: center;
    justify-content: center;
  }
  .artist-name {
    margin: 0;
    font-family: "Cabin", "Trebuchet MS", sans-serif;
    font-weight: 500;
    font-size: 38px;
    letter-spacing: 5px;
    color: var(--name-gold);
    text-transform: uppercase;
  }
  .title-band {
    position: absolute;
    left: 236px;
    top: 516px;
    width: 888px;
    height: 56px;
    background: var(--ink);
  }
  .title-art {
    position: absolute;
    inset: 0;
    width: 1200px;
    height: 1200px;
  }
  .title-lead {
    font-family: "Josefin Sans", "Futura", sans-serif;
    font-weight: 300;
    fill: var(--line-cream);
  }
  .title-main {
    font-family: "Uncial Antiqua", "Georgia", serif;
    fill: var(--ink);
  }
</style>
</head>
<body>
<main class="cover">
  <div class="cover-backdrop" role="img" aria-label="Painted textured background, dark umber with red streaks on the left fading into bright lime green on the right"></div>

  <div class="centre-artwork" role="img" aria-label="Central painted illustration in warm reds and oranges with collaged textures"></div>

  <div class="name-band">
    <p class="artist-name">Tom Halvery</p>
  </div>

  <div class="title-band"></div>

  <svg class="title-art" viewBox="0 0 1200 1200" aria-labelledby="releaseTitle">
    <title id="releaseTitle">Nobody Left the Lantern Burning</title>
    <text class="title-lead" x="248" y="562" font-size="44" textLength="680" lengthAdjust="spacing">NOBODY LEFT THE</text>
    <text class="title-main" x="244" y="662" font-size="96" textLength="876" lengthAdjust="spacingAndGlyphs">LANTERN BURNING</text>
  </svg>
</main>
</body>
</html>
```